lawn sign

Lawn Sign
Roofing Gutters Windows

Target Market(s)

roofing

Font styles to use
Sans Serif

Colors
86cfc6
33a6d7
fbee3f
faa54b

Requirements
Must have
• my logo
Nice to have
• designer for now

```html
<!DOCTYPE html>
<html lang="en">
<head>
<meta charset="utf-8">
<title>Lawn Sign – Roofing Gutters Windows</title>
<link rel="stylesheet" href="https://fonts.googleapis.com/css2?family=Ultra&display=swap">
<style>
  :root {
    --sign-white: #ffffff;
    --ray-green-strong: #a3cc4f;
    --ray-green-soft: #d9eab4;
    --headline-blue: #0d9ee0;
    --headline-shadow: #000000;
    --brand-dot: #9fcf5a;
  }
  html, body {
    margin: 0;
    padding: 0;
    width: 1200px;
    height: 920px;
    overflow: hidden;
    background: var(--sign-white);
  }
  .lawn-sign {
    position: relative;
    width: 1200px;
    height: 920px;
    overflow: hidden;
    background: var(--sign-white);
  }
  .sign-art {
    position: absolute;
    inset: 0;
    display: block;
  }
  .service-line {
    font-family: "Ultra", "Rockwell Extra Bold", "Rockwell", serif;
    font-size: 176px;
    fill: var(--headline-blue);
    stroke: var(--headline-blue);
    stroke-width: 5px;
    stroke-linejoin: round;
  }
  .service-line-shadow .service-line {
    fill: var(--headline-shadow);
    stroke: var(--headline-shadow);
  }
  .company-name {
    font-family: "Ultra", "Rockwell Extra Bold", "Rockwell", serif;
    font-size: 40px;
    fill: var(--headline-blue);
  }
  .company-dot { fill: var(--brand-dot); }
</style>
</head>
<body>
<main class="lawn-sign">
  <svg class="sign-art" width="1200" height="920" viewBox="0 0 1200 920" xmlns="http://www.w3.org/2000/svg">
    <defs>
      <radialGradient id="ray-glow" cx="700" cy="625" r="900" gradientUnits="userSpaceOnUse">
        <stop offset="0" stop-color="#ffffff"/>
        <stop offset="0.35" stop-color="#ffffff"/>
        <stop offset="0.75" stop-color="#d9eab4"/>
        <stop offset="1" stop-color="#a3cc4f"/>
      </radialGradient>
    </defs>

    <rect class="sunburst-backdrop" x="0" y="0" width="1200" height="920" fill="url(#ray-glow)"
          role="img" aria-label="Green sunburst rays radiating from the lower right, fading to white"/>

    <g class="service-list">
      <g class="service-line-shadow">
        <text class="service-line" x="80" y="188" textLength="744" lengthAdjust="spacingAndGlyphs">Roofing</text>
        <text class="service-line" x="80" y="368" textLength="690" lengthAdjust="spacingAndGlyphs">Gutters</text>
        <text class="service-line" x="86" y="554" textLength="846" lengthAdjust="spacingAndGlyphs">Windows</text>
      </g>
      <text class="service-line" x="72" y="180" textLength="744" lengthAdjust="spacingAndGlyphs">Roofing</text>
      <text class="service-line" x="72" y="360" textLength="690" lengthAdjust="spacingAndGlyphs">Gutters</text>
      <text class="service-line" x="78" y="546" textLength="846" lengthAdjust="spacingAndGlyphs">Windows</text>
    </g>

    <g class="company">
      <circle class="company-dot" cx="596" cy="842" r="24"/>
      <text class="company-name" x="640" y="856" textLength="500" lengthAdjust="spacingAndGlyphs">Larkfield Home Exteriors</text>
    </g>
  </svg>
</main>
</body>
</html>
```